Brochure Design - Non-Profit Fundraising Stream

We are a non-profit organization that is developing a fundraising project through the donation of life insurance policies. We have three brochures in each English and French that we developed for a sister organization that we want to reintegrate with our Foundation, keeping the same copy text just changing the logos, colors and make it overall more visually appealing. The foundation is called the 'Varnek-Holt Syndrome Foundation Canada'.
The original files in .docx format are attached as is the full logo and two symbol files. The deliverables would be six documents in total (InDesign or .docx), each brochure in English and French. The color hex codes are:
red: #7b2850
dark blue: #2c79a7
pale blue: #78b2e2

```html
<!DOCTYPE html>
<html lang="en">
<head>
<meta charset="utf-8">
<title>Varnek-Holt Syndrome Foundation Canada – Life Insurance Brochures</title>
<link href="https://fonts.googleapis.com/css2?family=Open+Sans:ital,wght@0,400;0,600;0,700;1,400;1,600&display=swap" rel="stylesheet">
<style>
:root{
  --red:#7b2850;
  --blue:#2c79a7;
  --pale:#78b2e2;
  --deep:#1f5f8c;
  --ink:#2b2f36;
  --stripe:#e3eef8;
  --canvas:#e9ebee;
  --paper:#ffffff;
}
*{margin:0;padding:0;box-sizing:border-box}
html,body{width:667px;height:1200px;overflow:hidden}
body{background:var(--canvas);font-family:"Open Sans",Arial,sans-serif;color:var(--ink);position:relative}
.page{position:absolute;width:287px;height:372px;background:var(--paper);box-shadow:0 1px 4px rgba(0,0,0,.18);overflow:hidden}
.p1{left:28px;top:16px}.p2{left:352px;top:16px}
.p3{left:28px;top:414px}.p4{left:352px;top:414px}
.p5{left:28px;top:812px}.p6{left:352px;top:812px}
.masthead{height:70px;background:linear-gradient(180deg,var(--pale) 0%,var(--blue) 100%);position:relative}
.brand{position:absolute;left:10px;top:8px;width:112px;height:54px;background:var(--paper);padding:7px 8px;display:flex;align-items:center;gap:5px}
.brand-dot{width:9px;height:9px;border-radius:50%;background:var(--red);flex:none}
.brand-name{font-size:8.5px;font-weight:600;color:var(--blue);line-height:1.15}
.doc-title{position:absolute;right:12px;top:20px;text-align:right;color:#fff;font-style:italic;font-size:8px;line-height:1.25}
.body{padding:9px 14px 0;font-size:4.6px;line-height:1.45}
.body p{margin-bottom:5px}
.lead{font-weight:600}
h4{font-size:5.4px;color:var(--blue);font-weight:700;margin:5px 0 3px}
ul{padding-left:10px;margin-bottom:5px}
.qa{border-top:.5px solid #c9d6e2}
.qa div{padding:2.5px 0;border-bottom:.5px solid #c9d6e2}
table{width:100%;border-collapse:collapse;font-size:4.4px;line-height:1.35}
th{background:var(--blue);color:#fff;text-align:left;padding:3px;font-weight:600}
td{padding:3.5px 3px;vertical-align:top;border-bottom:.5px solid #c9d6e2}
tr:nth-child(even) td{background:var(--stripe)}
td:first-child{width:42%;font-weight:600}
.footer{position:absolute;left:0;right:0;bottom:0;height:14px;background:var(--blue);color:#fff;font-size:4.2px;text-align:center;line-height:14px}
.split{display:flex;gap:8px}
.split .text{flex:1}
.callout{width:92px;background:var(--pale);color:#fff;padding:7px;font-size:4.6px;font-weight:600;align-self:flex-start;margin-top:4px}
.band{background:var(--blue);color:#fff;font-size:5.4px;font-weight:600;padding:3px 14px;margin:6px -14px 7px}
.flow{display:flex;align-items:center;justify-content:space-between;margin-bottom:8px}
.step{width:41px;height:32px;background:var(--deep);color:#fff;font-size:4.4px;text-align:center;display:flex;align-items:center;justify-content:center;padding:2px;line-height:1.25}
.arrow{width:8px;height:8px}
</style>
</head>
<body>

<!-- Page 1 -->
<section class="page p1">
  <header class="masthead">
    <div class="brand"><span class="brand-dot"></span><span class="brand-name">Varnek-Holt Syndrome Foundation Canada</span></div>
    <div class="doc-title">Donation of<br>Life Insurance</div>
  </header>
  <div class="body">
    <p class="lead">The Varnek-Holt Syndrome Foundation Canada welcomes gifts of life insurance. A policy gift can provide a large future donation at a modest cost today.</p>
    <h4>Ways to give</h4>
    <ul>
      <li>Name the Foundation as beneficiary</li>
      <li>Transfer ownership of a policy</li>
      <li>Buy a new policy for us</li>
      <li>Give an existing paid-up policy</li>
      <li>Add a rider to your plan</li>
      <li>Gift part of a group policy</li>
    </ul>
    <p>Please speak with your advisor before making any decision about a policy gift.</p>
    <h4>Frequently asked</h4>
    <div class="qa">
      <div>Will I receive a tax receipt for this gift?</div>
      <div>Can I change the beneficiary at a later date?</div>
      <div>Who pays the premiums after the transfer?</div>
      <div>Is a medical exam needed for new policies?</div>
      <div>How is the value of my policy set?</div>
      <div>Can several donors share a single policy?</div>
    </div>
  </div>
  <footer class="footer">varnekholt.ca · info@varnekholt.ca · Charity registered</footer>
</section>

<!-- Page 2 -->
<section class="page p2">
  <header class="masthead">
    <div class="brand"><span class="brand-dot"></span><span class="brand-name">Varnek-Holt Syndrome Foundation Canada</span></div>
    <div class="doc-title">Don d'une<br>assurance vie</div>
  </header>
  <div class="body">
    <p class="lead">La Fondation canadienne du syndrome de Varnek-Holt accepte les dons d'assurance vie. Un tel don offre un grand soutien futur à un coût modeste.</p>
    <h4>Façons de donner</h4>
    <ul>
      <li>Nommer la Fondation bénéficiaire</li>
      <li>Céder la propriété d'une police</li>
      <li>Souscrire une nouvelle police</li>
      <li>Donner une police libérée</li>
      <li>Ajouter un avenant au contrat</li>
      <li>Donner une part d'assurance collective</li>
    </ul>
    <p>Consultez votre conseiller avant de prendre une décision au sujet d'un don.</p>
    <h4>Questions fréquentes</h4>
    <div class="qa">
      <div>Vais-je recevoir un reçu fiscal pour ce don?</div>
      <div>Puis-je changer le bénéficiaire plus tard?</div>
      <div>Qui paie les primes après la cession?</div>
      <div>Un examen médical est-il requis?</div>
      <div>Comment la valeur de la police est-elle fixée?</div>
      <div>Plusieurs donateurs peuvent-ils partager une police?</div>
    </div>
  </div>
  <footer class="footer">varnekholt.ca · info@varnekholt.ca · Organisme enregistré</footer>
</section>

<!-- Page 3 -->
<section class="page p3">
  <header class="masthead">
    <div class="brand"><span class="brand-dot"></span><span class="brand-name">Varnek-Holt Syndrome Foundation Canada</span></div>
    <div class="doc-title">Gift Options<br>at a Glance</div>
  </header>
  <div class="body">
    <table>
      <tr><th>Option</th><th>What it means for you</th></tr>
      <tr><td>New policy owned by us</td><td>Premiums you pay are receipted each year.</td></tr>
      <tr><td>Existing policy transferred</td><td>Cash value is receipted at the time of transfer.</td></tr>
      <tr><td>Foundation as beneficiary</td><td>Your estate receives a receipt for the death benefit.</td></tr>
      <tr><td>Paid-up policy</td><td>No further premiums; receipt for fair market value.</td></tr>
      <tr><td>Group insurance</td><td>Name us on an employer plan at no cost.</td></tr>
      <tr><td>Partial beneficiary</td><td>Share the benefit between family and the Foundation.</td></tr>
      <tr><td>Policy rider</td><td>Add coverage to an existing plan for our work.</td></tr>
      <tr><td>Joint last-to-die</td><td>Lower premiums; benefit paid after both lives.</td></tr>
      <tr><td>Term to permanent</td><td>Convert coverage and then gift the new policy.</td></tr>
      <tr><td>Memorial gift</td><td>Honour a loved one with a named research fund.</td></tr>
    </table>
  </div>
  <footer class="footer">varnekholt.ca · info@varnekholt.ca · Charity registered</footer>
</section>

<!-- Page 4 -->
<section class="page p4">
  <header class="masthead">
    <div class="brand"><span class="brand-dot"></span><span class="brand-name">Varnek-Holt Syndrome Foundation Canada</span></div>
    <div class="doc-title">Options de dons<br>en un coup d'œil</div>
  </header>
  <div class="body">
    <table>
      <tr><th>Option</th><th>Ce que cela signifie pour vous</th></tr>
      <tr><td>Nouvelle police à notre nom</td><td>Les primes payées donnent un reçu chaque année.</td></tr>
      <tr><td>Police existante cédée</td><td>La valeur de rachat est reçue au transfert.</td></tr>
      <tr><td>Fondation bénéficiaire</td><td>Votre succession reçoit un reçu pour la prestation.</td></tr>
      <tr><td>Police libérée</td><td>Aucune prime; reçu pour la juste valeur marchande.</td></tr>
      <tr><td>Assurance collective</td><td>Nommez-nous sur le régime de l'employeur.</td></tr>
      <tr><td>Bénéficiaire partiel</td><td>Partagez la prestation entre famille et Fondation.</td></tr>
      <tr><td>Avenant</td><td>Ajoutez une couverture à un contrat existant.</td></tr>
      <tr><td>Conjointe au dernier décès</td><td>Primes réduites; prestation après les deux vies.</td></tr>
      <tr><td>Temporaire à permanente</td><td>Convertissez, puis donnez la nouvelle police.</td></tr>
      <tr><td>Don commémoratif</td><td>Honorez un proche par un fonds de recherche.</td></tr>
    </table>
  </div>
  <footer class="footer">varnekholt.ca · info@varnekholt.ca · Organisme enregistré</footer>
</section>

<!-- Page 5 -->
<section class="page p5">
  <header class="masthead">
    <div class="brand"><span class="brand-dot"></span><span class="brand-name">Varnek-Holt Syndrome Foundation Canada</span></div>
    <div class="doc-title">How Your<br>Gift Works</div>
  </header>
  <div class="body">
    <h4>Planning your life insurance gift</h4>
    <div class="split">
      <div class="text">
        <p>A life insurance gift lets you make a lasting difference for people living with Varnek-Holt syndrome. Your gift funds research, clinical care networks and family support programs across Canada for years to come.</p>
        <p>We work with you and your advisor to choose the option that best fits your goals, your family and your tax planning needs.</p>
      </div>
      <div class="callout">Every policy gift brings us closer to better care and answers for families.</div>
    </div>
    <div class="band">The process</div>
    <div class="flow">
      <div class="step">Talk with your advisor</div>
      <svg class="arrow" viewBox="0 0 8 8"><path d="M1 1 L7 4 L1 7 Z" fill="var(--pale)"/></svg>
      <div class="step">Choose a gift option</div>
      <svg class="arrow" viewBox="0 0 8 8"><path d="M1 1 L7 4 L1 7 Z" fill="var(--pale)"/></svg>
      <div class="step">Contact the Foundation</div>
      <svg class="arrow" viewBox="0 0 8 8"><path d="M1 1 L7 4 L1 7 Z" fill="var(--pale)"/></svg>
      <div class="step">Complete the forms</div>
      <svg class="arrow" viewBox="0 0 8 8"><path d="M1 1 L7 4 L1 7 Z" fill="var(--pale)"/></svg>
      <div class="step">Receive your receipt</div>
    </div>
    <p>Thank you for thinking of us. Our team is glad to answer your questions at any stage of planning.</p>
  </div>
  <footer class="footer">varnekholt.ca · info@varnekholt.ca · Charity registered</footer>
</section>

<!-- Page 6 -->
<section class="page p6">
  <header class="masthead">
    <div class="brand"><span class="brand-dot"></span><span class="brand-name">Varnek-Holt Syndrome Foundation Canada</span></div>
    <div class="doc-title">Fonctionnement<br>de votre don</div>
  </header>
  <div class="body">
    <h4>Planifier votre don d'assurance vie</h4>
    <div class="split">
      <div class="text">
        <p>Un don d'assurance vie vous permet d'aider durablement les personnes atteintes du syndrome de Varnek-Holt. Il finance la recherche, les soins cliniques et le soutien aux familles partout au Canada.</p>
        <p>Nous travaillons avec vous et votre conseiller pour choisir l'option qui répond à vos objectifs et à votre planification fiscale.</p>
      </div>
      <div class="callout">Chaque don d'assurance nous rapproche de meilleurs soins pour les familles.</div>
    </div>
    <div class="band">Les étapes</div>
    <div class="flow">
      <div class="step">Parlez à votre conseiller</div>
      <svg class="arrow" viewBox="0 0 8 8"><path d="M1 1 L7 4 L1 7 Z" fill="var(--pale)"/></svg>
      <div class="step">Choisissez une option</div>
      <svg class="arrow" viewBox="0 0 8 8"><path d="M1 1 L7 4 L1 7 Z" fill="var(--pale)"/></svg>
      <div class="step">Contactez la Fondation</div>
      <svg class="arrow" viewBox="0 0 8 8"><path d="M1 1 L7 4 L1 7 Z" fill="var(--pale)"/></svg>
      <div class="step">Remplissez les formulaires</div>
      <svg class="arrow" viewBox="0 0 8 8"><path d="M1 1 L7 4 L1 7 Z" fill="var(--pale)"/></svg>
      <div class="step">Recevez votre reçu</div>
    </div>
    <p>Merci de penser à nous. Notre équipe répondra volontiers à vos questions à chaque étape.</p>
  </div>
  <footer class="footer">varnekholt.ca · info@varnekholt.ca · Organisme enregistré</footer>
</section>

</body>
</html>
```